The Brightleaf Network of Sites
Brightleaf, Inc.
Creative Brief
Fund Raising
Charities and non-profits
Brochure will give an overview of the following services: Tallowmark.com PresentPassHarbor.org Dotwillow.com Pagefernly.com Brightleaf Rewards program

```html
<!DOCTYPE html>
<html lang="en">
<head>
<meta charset="utf-8">
<title>Brightleaf Inc. – Trifold Brochure</title>
<link rel="stylesheet" href="https://fonts.googleapis.com/css2?family=Arimo:wght@400;700&family=Michroma&family=Courgette&display=swap">
<style>
:root{
  --gold:#f7c300;
  --gold-light:#ffe873;
  --gold-deep:#e09a00;
  --ink:#111;
  --black:#000;
  --white:#fff;
  --red:#d8141b;
  --grey:#2b2b2b;
}
*{box-sizing:border-box;margin:0;padding:0}
html,body{width:1200px;height:850px;overflow:hidden;background:#fff}
.brochure{position:relative;width:1200px;height:850px;display:flex;font-family:Arimo,Arial,sans-serif}
.panel{position:relative;width:400px;height:850px;overflow:hidden}

/* left panel */
.panel--services{background:linear-gradient(180deg,var(--gold-light),var(--gold) 45%,var(--gold-deep));border-right:3px solid var(--black)}
.service{position:absolute;left:0;width:397px}
.service__title{color:var(--white);font-weight:700;font-size:19px;letter-spacing:.3px;white-space:nowrap}
.service__url{color:var(--gold);font-weight:700;font-size:13px;margin-top:4px}
.service__body{font-size:15px;line-height:1.32;color:var(--ink)}
.photo{position:absolute}

.walk{top:0;height:240px}
.walk .photo{left:0;top:0;width:150px;height:240px;background:linear-gradient(160deg,#c9c3b6,#6d6a66)}
.walk__head{position:absolute;left:150px;top:0;width:247px;height:72px;background:var(--grey);padding:20px 0 0 22px}
.walk .service__body{position:absolute;left:165px;top:88px;width:225px}

.books{top:245px;height:150px}
.books__head{background:var(--grey);height:62px;padding:11px 0 0 20px}
.books__head .service__url{padding-left:100px}
.books .service__body{position:absolute;left:20px;top:76px;width:215px}
.books .photo{right:28px;top:74px;width:110px;height:64px;background:linear-gradient(180deg,#e8b4c8,#5fb3d9)}

.dating{top:400px;height:450px;background:var(--black)}
.dating__head{height:50px;padding:14px 0 0 145px;background:var(--grey)}
.dating .photo{left:0;top:50px;width:190px;height:400px;background:linear-gradient(180deg,#5b6f86,#c48b55 70%,#3a2a1e)}
.dating .service__body{position:absolute;left:205px;top:72px;width:185px;color:var(--white)}
.info-box{position:absolute;left:30px;bottom:18px;width:220px;height:84px;background:rgba(20,20,20,.92);border:1px solid #444;text-align:center;color:var(--white);font-size:13px;padding-top:8px;line-height:1.32}
.info-box strong{color:var(--gold)}

/* middle panel */
.panel--cover{background:radial-gradient(ellipse at 50% 40%,var(--gold-light),var(--gold) 55%,var(--gold-deep));border-right:3px solid var(--black)}
.brand-mark{display:block;margin:0 auto;width:46px;height:46px;background:var(--black);border:2px solid var(--gold-deep)}
.panel--cover .brand-mark{margin-top:34px}
.cover__name{text-align:center;font-family:Michroma,sans-serif;font-size:28px;color:var(--ink);margin-top:16px;white-space:nowrap}
.compass{position:absolute;left:70px;top:205px;width:257px;height:300px;border-radius:6px;background:linear-gradient(180deg,rgba(40,60,140,.35),rgba(40,60,140,.18) 60%,rgba(224,154,0,.25))}
.tagline{position:absolute;left:0;width:397px;top:520px;text-align:center;font-family:Courgette,cursive;color:var(--ink)}
.tagline span{display:block;font-size:26px}
.tagline em{display:block;font-style:normal;font-size:46px;line-height:1.05}
.contact{position:absolute;left:0;bottom:0;width:397px;height:145px;background:var(--black);color:var(--white);padding:16px 34px;font-size:13.5px;line-height:1.4}
.contact b{font-weight:700}
.contact__row{display:flex;gap:22px;margin-top:14px;color:var(--gold);font-weight:700;font-size:14px}
.contact__item{display:flex;align-items:center;gap:6px}
.contact__web{text-align:center;margin-top:14px;color:var(--gold);font-size:12px}

/* right panel */
.panel--front{background:var(--black)}
.front__band{height:150px;background:linear-gradient(180deg,var(--gold-light),var(--gold) 60%,var(--gold-deep));text-align:center;padding-top:26px}
.front__band .brand-mark{width:44px;height:44px}
.front__name{font-family:Michroma,sans-serif;font-size:26px;color:var(--ink);margin-top:12px;white-space:nowrap}
.front__slogan{color:var(--red);font-size:13px;font-weight:700}
.hands{position:absolute;right:0;top:156px;width:384px;height:324px;background:linear-gradient(160deg,#1a1411,#6e4a3a 45%,#b88870 70%,#2a1d17)}
.audiences{position:absolute;left:30px;top:486px;font-family:Courgette,cursive;color:var(--gold);line-height:1.2}
.audiences .a1{font-size:34px}
.audiences .a2{font-size:26px;padding-left:10px}
.audiences .a3{font-size:36px;padding-left:140px}
.front__pitch{position:absolute;left:30px;top:735px;width:350px;color:var(--white);font-size:15px;line-height:1.3}
.front__pitch b{color:var(--gold)}
.front__web{position:absolute;left:0;width:400px;bottom:14px;text-align:center;color:var(--gold);font-size:12px}
</style>
</head>
<body>
<main class="brochure">

  <section class="panel panel--services">
    <article class="service walk">
      <div class="photo" role="img" aria-label="Photo of runners in a charity road race"></div>
      <div class="walk__head">
        <h2 class="service__title">RUN A WALKATHON</h2>
        <p class="service__url">http://stridewell.com</p>
      </div>
      <p class="service__body">Walkathons are one of the easiest fundraisers for charities and causes. Let us guide you through the process and allow for online corporate and supporter sponsorship.</p>
    </article>

    <article class="service books">
      <div class="books__head">
        <h2 class="service__title">RUN A BOOKATHON / BOOKFAIR</h2>
        <p class="service__url">http://pagefernly.com</p>
      </div>
      <p class="service__body">Set up a Bookathon or have supporters purchase books online to help raise funds.</p>
      <div class="photo" role="img" aria-label="Photo of a stack of colourful books"></div>
    </article>

    <article class="service dating">
      <div class="dating__head"><h2 class="service__title">KINDREDLOOP.COM</h2></div>
      <div class="photo" role="img" aria-label="Photo of a couple walking on a beach at sunset"></div>
      <p class="service__body">KindredLoop is the fastest growing relationship site on the web. Create your kindredloop profile to begin the exciting journey towards finding your match.</p>
      <div class="info-box">For more information on<br><strong>The Brightleaf CharityNetwork</strong><br>please visit<br><strong>www.brightleaf.co</strong></div>
    </article>
  </section>

  <section class="panel panel--cover">
    <span class="brand-mark"></span>
    <h1 class="cover__name">Brightleaf Inc.</h1>
    <div class="compass" role="img" aria-label="Illustration of a compass rose"></div>
    <p class="tagline"><span>Your Moral</span><em>Compass</em></p>
    <footer class="contact">
      <p><b>For more details please contact</b> one of our dedicated fund raising specialists at :</p>
      <div class="contact__row">
        <span class="contact__item">
          <svg width="18" height="18" viewBox="0 0 24 24"><path fill="#f7c300" d="M6.6 10.8a15 15 0 0 0 6.6 6.6l2.2-2.2a1 1 0 0 1 1-.25 11 11 0 0 0 3.6.6 1 1 0 0 1 1 1V20a1 1 0 0 1-1 1A17 17 0 0 1 3 4a1 1 0 0 1 1-1h3.5a1 1 0 0 1 1 1 11 11 0 0 0 .6 3.6 1 1 0 0 1-.25 1z"/></svg>
          555-Donate-0</span>
        <span class="contact__item">
          <svg width="18" height="14" viewBox="0 0 24 18"><rect x="1" y="1" width="22" height="16" rx="2" fill="none" stroke="#f7c300" stroke-width="2"/><path d="M1 2l11 8 11-8" fill="none" stroke="#f7c300" stroke-width="2"/></svg>
          support@brightleaf.us</span>
      </div>
      <p class="contact__web">www.brightleaf.co</p>
    </footer>
  </section>

  <section class="panel panel--front">
    <header class="front__band">
      <span class="brand-mark"></span>
      <h2 class="front__name">Brightleaf Inc.</h2>
      <p class="front__slogan">Live Life.Do Good</p>
    </header>
    <div class="hands" role="img" aria-label="Photo of joined hands holding a red heart"></div>
    <p class="audiences"><span class="a1">Charities</span><br><span class="a2">Non-Profit Organizations</span><br><span class="a3">&amp; Schools</span></p>
    <p class="front__pitch"><b>Brightleaf</b> gives you all the tools you need to be successful and create an online presence unlike any other.</p>
    <p class="front__web">www.brightleaf.co</p>
  </section>

</main>
</body>
</html>
```